This is a label for a new sake made in Japan imported into Aust

This will be a bottle label for a new sake imported into Australia. The hero of the label is the Trelu. We have joined the "O" meaning great in Japanese and used sake with "Z" to have Trelu with the play on words using Oz as in our slang for Aussie. A modern label with a Japanese take is key. This is a premium sake made in Japan for the Australian market.
The "Lark Hollow" up the top is the name of the company, we have yet to design a logo for the company.

Target Market(s)

Alcohol

Logo Text

Trelu

Font styles to use
Serif

Requirements
Must have
• easy to read, with a hint of Japanese origin
Should not have
• too busy

```html
<!DOCTYPE html>
<html lang="en">
<head>
<meta charset="utf-8">
<title>Trelu – Premium Japanese Sake label</title>
<link href="https://fonts.googleapis.com/css2?family=Shippori+Mincho:wght@500;700;800&display=swap" rel="stylesheet">
<style>
  :root {
    --backdrop: #fcdcc8;
    --label-paper: #fbebf5;
    --petal-wash: rgba(246, 233, 200, 0.55);
    --gold-light: #f1f48c;
    --gold-mid: #e6d45a;
    --gold-deep: #c9a02a;
    --ink: #111111;
    --sake-red: #b20b05;
    --tag-text: #ffffff;
  }
  * { box-sizing: border-box; margin: 0; padding: 0; }
  html, body {
    width: 1200px;
    height: 1197px;
    overflow: hidden;
    background: var(--backdrop);
  }
  .canvas {
    position: relative;
    width: 1200px;
    height: 1197px;
    display: flex;
    align-items: center;
    justify-content: center;
  }
  .label {
    position: relative;
    width: 1000px;
    height: 760px;
    background: var(--label-paper);
    overflow: hidden;
    font-family: "Shippori Mincho", "Times New Roman", serif;
  }
  .label__petals {
    position: absolute;
    inset: 170px 0 70px 0;
    background: linear-gradient(160deg, transparent 10%, var(--petal-wash) 45%, transparent 60%, var(--petal-wash) 85%, transparent 100%);
  }
  .label__top-band {
    position: absolute;
    top: 0;
    left: 0;
    width: 1000px;
    height: 170px;
  }
  .label__company {
    position: absolute;
    top: 44px;
    left: 0;
    width: 100%;
    text-align: center;
    font-size: 44px;
    font-weight: 500;
    color: var(--ink);
    letter-spacing: 1px;
  }
  .label__name {
    position: absolute;
    top: 210px;
    left: 0;
    width: 100%;
    text-align: center;
    font-size: 230px;
    line-height: 1.1;
    font-weight: 800;
    color: var(--ink);
    letter-spacing: 4px;
  }
  .label__tag {
    position: absolute;
    top: 540px;
    left: 50%;
    transform: translateX(-50%);
    background: var(--sake-red);
    color: var(--tag-text);
    font-size: 40px;
    font-weight: 500;
    padding: 8px 44px 12px;
    white-space: nowrap;
    letter-spacing: 1px;
  }
  .label__bottom-band {
    position: absolute;
    left: 0;
    bottom: 52px;
    width: 100%;
    height: 22px;
    background: linear-gradient(90deg, var(--gold-mid), var(--gold-light) 45%, var(--gold-mid) 70%, var(--gold-deep));
  }
</style>
</head>
<body>
  <main class="canvas">
    <section class="label">
      <div class="label__petals" role="img" aria-label="Drifting pale cream cherry blossom petals across the label"></div>

      <svg class="label__top-band" viewBox="0 0 1000 170" aria-hidden="true">
        <defs>
          <linearGradient id="goldSheen" x1="0" x2="1" y1="0" y2="0">
            <stop offset="0" stop-color="#e6d45a"/>
            <stop offset="0.5" stop-color="#f1f48c"/>
            <stop offset="0.8" stop-color="#e6d45a"/>
            <stop offset="1" stop-color="#c9a02a"/>
          </linearGradient>
        </defs>
        <path d="M0 28 H250 C290 28 300 130 380 130 H620 C700 130 710 28 750 28 H1000 V52 H756 C730 52 720 150 624 150 H376 C280 150 270 52 244 52 H0 Z" fill="url(#goldSheen)"/>
        <path d="M250 0 H750 C710 0 700 130 620 130 H380 C300 130 290 0 250 0 Z" fill="url(#goldSheen)" opacity="0.85"/>
      </svg>
      <p class="label__company">Lark Hollow</p>

      <h1 class="label__name">Trelu</h1>
      <p class="label__tag">Premium Japanese Sake</p>

      <div class="label__bottom-band"></div>
    </section>
  </main>
</body>
</html>
```